Fast Growing Personal Injury Law Firm Needs Business Card Design

We need a business card design for a fast growing personal injury law firm in Florida. Our name is Darren Kolvisty, P.A. Our practice is comprised of younger attorneys (in their 30s) that employ more modern techniques/tools than our older competition. We would prefer a look that is a modern play on a classic look. Also, we would like to continue using a color scheme that employs navy blue and kelly green (other shades of green could be fine too) as well as our "E" logo.

Industry/Entity Type

Law Firm

```html
<!DOCTYPE html>
<html lang="en">
<head>
<meta charset="utf-8">
<title>Darren Kolvisty, P.A. — Business Card</title>
<link rel="stylesheet" href="https://fonts.googleapis.com/css2?family=Cinzel:wght@400;600&family=Crimson+Text&display=swap">
<style>
  :root {
    --green: #0b8a3f;
    --navy: #012b5e;
    --paper: #ffffff;
    --edge: #8a8a8a;
    --shadow: rgba(0,0,0,0.28);
  }
  html, body { margin: 0; padding: 0; overflow: hidden; }
  body { width: 1200px; height: 1200px; background: var(--paper); position: relative; }
  .card { position: absolute; left: 316px; width: 552px; height: 312px; box-sizing: border-box; box-shadow: 8px 10px 12px var(--shadow); }
  .card-front { top: 175px; background: var(--paper); border: 1.5px solid var(--edge); }
  .card-back { top: 630px; background: var(--navy); }
  .abs { position: absolute; margin: 0; white-space: nowrap; }

  .brand-mark { left: 36px; top: 32px; width: 80px; height: 78px; background: var(--green); }
  .brand-name { left: 140px; top: 36px; font: 600 31px/1 'Cinzel', serif; color: var(--green); letter-spacing: 1px; }
  .brand-tagline { left: 140px; top: 76px; font: 400 18px/1 'Cinzel', serif; color: var(--navy); letter-spacing: 3px; }

  .firm-name { left: 36px; top: 196px; font: 600 19px/1 'Cinzel', serif; color: var(--green); letter-spacing: 0.5px; }
  .firm-role { left: 74px; top: 220px; font: 400 11px/1 'Cinzel', serif; color: var(--navy); letter-spacing: 2px; }
  .firm-address { left: 36px; top: 248px; font: 400 10px/13px 'Cinzel', serif; color: var(--navy); letter-spacing: 1.6px; }

  .divider { left: 304px; top: 197px; width: 2px; height: 74px; background: var(--green); }

  .contact-list { left: 344px; top: 197px; list-style: none; padding: 0; }
  .contact-item { display: flex; align-items: center; height: 27px; font: 400 14px/1 'Crimson Text', serif; color: var(--navy); letter-spacing: 0.5px; }
  .contact-key { width: 18px; height: 18px; margin-right: 6px; background: var(--green); color: var(--paper); font: 600 12px/18px 'Cinzel', serif; text-align: center; }

  .back-mark { left: 144px; top: 98px; width: 90px; height: 90px; background: var(--green); }
  .back-name { left: 252px; top: 130px; font: 600 24px/1 'Cinzel', serif; color: var(--paper); letter-spacing: 1px; }
  .back-email { left: 0; width: 552px; top: 272px; text-align: center; font: 400 14px/1 'Cinzel', serif; color: var(--green); letter-spacing: 2.5px; }
</style>
</head>
<body>
  <section class="card card-front">
    <div class="abs brand-mark"></div>
    <h1 class="abs brand-name">Darren Kolvisty, P.A.</h1>
    <p class="abs brand-tagline">Personal Injury Attorneys</p>

    <h2 class="abs firm-name">Darren Kolvisty, P.A.</h2>
    <p class="abs firm-role">Attorney at Law</p>
    <address class="abs firm-address" style="font-style:normal">1250 Harbor Point Drive Suite 210<br>Lakeview Landing, Florida 34000</address>

    <div class="abs divider"></div>

    <ul class="abs contact-list">
      <li class="contact-item"><span class="contact-key">P</span>555.014.2200</li>
      <li class="contact-item"><span class="contact-key">F</span>555.014.2201</li>
      <li class="contact-item"><span class="contact-key">W</span>KOLVISTYLAW.COM</li>
    </ul>
  </section>

  <section class="card card-back">
    <div class="abs back-mark"></div>
    <p class="abs back-name">Darren Kolvisty</p>
    <p class="abs back-email">darren@kolvistylaw.com</p>
  </section>
</body>
</html>
```